Bertrand Music Video and Film Production

THE FLYER SHOULD INCLUDE THIS TEXT:

"PROFESSIONAL FILM AND MUSIC VIDEO DIRECTzOR WITH OVER 10 YEARS EXPERIENCE. CLIENT LIST INCLUDES, 714, MARWICK, PALE HARBOURS, BRAMBLEGATE, THE LANTERNS, BLUE OAK, TAMSIN-JO, NELL MARIS, QRV, WILLOWTREE.
HD, SUPER 8, LIVE DVD, PROMO REELS AND VIDEOS ON TIME AND ON BUDGET."

I need to create a flyer/ad that I will use to promote myself and the services I provide.

My name is Bertrand Vellacott and I am a music video clip director and editor that can achieve great results regardless of budgets.

Working with HD and Super 8 vintage film formats to achieve the look you want.

I am a Melbourne based film maker with a huge client list; 714, Marwick, Pale Harbours, Nell Maris, Tamsin-Jo, Bramblegate, The Lanterns, Dominic Plaskett, Willowtree Marketing, QRV and Carrowvale Shire Council.

Black and white classic design. Clean and neat not too busy, almost minimal in a way. Incorpirate my initials to create a logo perhaps.

It needs to appeal and relate to various music genres including; rock, pop, soul, funk, country and folk as I make music videos for artists of many genres.

Feature my website:

www.clipvaultia.com/bertvella

Include my email address

bertrandvellacott@mailzephra.com

Many thanks

Bertrand

Target Market(s)

Music artists and bands performing all sorts of music styles from; rock, soul, funk, pop, country and folk.

Appealing also to band managers, artist representation and record labels/music publishers.

Industry/Entity Type

Artists

Requirements
Must have
• My website and email address and my name. I am a sole trader so i don't have a business name as such, just my name, Bertrand Vellacott.
Should not have
• a picture of me

```html
<!DOCTYPE html>
<html lang="en">
<head>
<meta charset="utf-8">
<title>Bertrand Vellacott – Film and Music Video Director</title>
<link href="https://fonts.googleapis.com/css2?family=PT+Sans:wght@400;700&family=Open+Sans:wght@400;700;800&display=swap" rel="stylesheet">
<style>
  :root {
    --backdrop: #1c1c1c;
    --paper: #ffffff;
    --brand-blue: #1f6fbd;
    --ink: #111111;
    --body-grey: #8a8a8a;
    --panel-grey: #e6e6e6;
    --shape-grey: #8f8f8f;
    --art-light: #ececec;
    --art-mid: #c4c4c4;
  }
  * { margin: 0; padding: 0; box-sizing: border-box; }
  html, body {
    width: 1200px; height: 817px; overflow: hidden;
    background: var(--backdrop);
  }
  .flyer {
    position: absolute; left: 426px; top: 17px;
    width: 348px; height: 782px;
    background: var(--paper);
    overflow: hidden;
    font-family: "Open Sans", "PT Sans", sans-serif;
  }
  .artwork {
    position: absolute; left: 0; top: 36px; width: 348px; height: 330px;
    background: linear-gradient(160deg, var(--art-light) 0%, #d6d6d6 55%, var(--art-mid) 100%);
    opacity: 0.85;
  }
  .shapes { position: absolute; left: 0; top: 0; width: 348px; height: 782px; }
  .name-band {
    position: absolute; left: 22px; top: 23px; right: 0; height: 68px;
    background: var(--brand-blue);
    color: var(--paper);
    font-family: "PT Sans", sans-serif;
    font-size: 37px; line-height: 68px;
    padding-left: 12px; white-space: nowrap;
  }
  .pitch {
    position: absolute; left: 72px; top: 355px; width: 270px;
    color: var(--body-grey);
    text-transform: uppercase;
  }
  .pitch .kicker { color: var(--ink); font-weight: 800; font-size: 12px; line-height: 14px; }
  .pitch .headline {
    color: var(--ink); font-weight: 800; font-size: 26px; line-height: 26px;
    letter-spacing: -0.5px; margin-top: 1px;
  }
  .pitch .experience { font-size: 12px; line-height: 15px; margin-top: 2px; }
  .pitch .experience strong, .pitch .services strong { color: #444; font-weight: 800; }
  .pitch .clients { font-size: 11.5px; line-height: 15.5px; }
  .pitch .services { font-size: 15px; line-height: 19px; margin-top: 6px; }
  .contact {
    position: absolute; left: 0; right: 0; top: 688px;
    text-align: center; color: #333;
    font-size: 12px; line-height: 19px;
  }
</style>
</head>
<body>
  <main class="flyer">
    <div class="artwork" role="img" aria-label="Faded grey illustration of a vintage studio microphone and a film reel"></div>
    <svg class="shapes" viewBox="0 0 348 782" aria-hidden="true">
      <polygon points="0,372 55,362 55,680 0,650" fill="var(--shape-grey)"/>
      <polygon points="38,322 336,333 336,658 57,671" fill="var(--panel-grey)"/>
    </svg>
    <h1 class="name-band">Bertrand Vellacott</h1>
    <section class="pitch">
      <p class="kicker">Professional</p>
      <h2 class="headline">Film and Music<br>Video Director</h2>
      <p class="experience">With over <strong>10 years experience</strong>.</p>
      <p class="clients">Client list includes, 714, Marwick, Pale Harbours, Bramblegate, The Lanterns, Blue Oak, Tamsin-Jo, Nell Maris, QRV, Willowtree.</p>
      <p class="services">HD, Super 8, Live DVD, Promo reels and videos <strong>on time</strong> and <strong>on budget</strong></p>
    </section>
    <footer class="contact">
      <p>www.clipvaultia.com/bertvella</p>
      <p>bertrandvellacott@mailzephra.com</p>
    </footer>
  </main>
</body>
</html>
```